Psychotherapy and emotion coaching with vaLumo requires web design

I need a web design for emotion coaching (release of emotional blockages) (psychotherapy) with the target group trauma-related disorders and anxiety disorders. The website should be clear and well-organized, i.e. rather simple. The colors should be light, blue, green and yellow are desirable. The design should radiate security.

A logo already exists and should be used appropriately.

Three columns should describe the following
-Emotion regulation
-Imaginative structure constellations
-Ego-State-Therapy

An outdated draft can be seen here:
www.ruhiger-morgen.de
The website should advertise coded in Wordpress.

I need the landing page, for which there are drafts now, and at least one more page (maybe a template) for further information (like "About me")

Target Market(s)

Clients for coaching and therapy with trauma or axienty disorders;

Coding

Coded - Design and coding required

Number of Pages Required

3 page

Font styles to use
Sans Serif

Colors
0054AA
0677BA
7BADD7
CADEEF
E8F1F8
59FF00
82FF00
B8FF75
E3FFCB
F4FFEA
FFF300
FFF600
FEFA6F
FFFEC7
FFFEE8

Requirements
Nice to have
• Title: "More happiness and satisfaction in life"
Should not have
• "Therapy" should not be listed in the header; Instead "More happiness and satisfaction in life"

```html
<!DOCTYPE html>
<html lang="de">
<head>
<meta charset="utf-8">
<title>Achtsam Leben – Mehr Glück und Zufriedenheit im Leben</title>
<link href="https://fonts.googleapis.com/css2?family=Plus+Jakarta+Sans:wght@400;500;600;700&family=Poppins:wght@500;600;800&family=Rufina:wght@700&display=swap" rel="stylesheet">
<style>
:root{
  --blue:#0054aa;
  --blue-mid:#0677ba;
  --blue-light:#7badd7;
  --blue-pale:#e8f1f8;
  --green:#4caf50;
  --yellow:#f5c518;
  --yellow-strong:#fdb813;
  --ink:#1c1c1c;
  --text:#4a4a4a;
  --grey-bg:#f6f6f6;
  --card-grey:#ececec;
  --white:#fff;
}
*{box-sizing:border-box;margin:0;padding:0}
html,body{width:1200px;height:5063px;overflow:hidden}
body{position:relative;font-family:"Plus Jakarta Sans",sans-serif;color:var(--text);background:var(--white)}
.abs{position:absolute}
.btn{position:absolute;display:flex;align-items:center;justify-content:center;font-weight:700;font-size:13px;border-radius:4px;background:var(--blue);color:var(--white);border:0}
.brand{display:flex;align-items:center;gap:14px;font-family:"Plus Jakarta Sans",sans-serif;font-weight:600;font-size:19px}
.brand-mark{width:34px;height:34px;border-radius:50%;background:var(--yellow)}
.hex{clip-path:polygon(50% 0,100% 25%,100% 75%,50% 100%,0 75%,0 25%)}
p.body{font-size:13.5px;line-height:23px;color:var(--text)}
h2.svc{font-family:"Plus Jakarta Sans",sans-serif;font-weight:600;font-size:28px;color:var(--ink)}

/* hero */
.hero{left:0;top:0;width:1200px;height:610px;background:linear-gradient(180deg,#eef1f2 0%,#d9dcd6 35%,#b8a77a 62%,#8d7a4c 100%)}
.hero-title{left:140px;top:212px;font-family:"Rufina",serif;font-size:54px;line-height:70px;color:var(--white);text-transform:capitalize}
.down{left:578px;top:610px;width:46px;height:52px;background:var(--blue)}

/* issue */
.issue{left:0;top:682px;width:1200px;height:553px;background:var(--grey-bg)}
.issue h1{position:absolute;left:137px;top:45px;width:480px;font-family:"Plus Jakarta Sans",sans-serif;font-weight:500;font-size:29px;line-height:40px;color:var(--ink)}
.benefit{position:absolute;display:flex;align-items:center;gap:10px;font-size:12.5px;font-weight:600;color:var(--ink)}
.tick{width:18px;height:18px}

/* testimonials */
.reviews{left:0;top:3520px;width:1200px;height:425px;background:var(--grey-bg)}
.card{position:absolute;top:155px;width:295px;height:187px;border:2px solid var(--blue);border-radius:3px;background:var(--white);padding:42px 22px 0}
.card p{font-size:13px;line-height:23px;color:var(--text)}
.card .rule{width:72px;height:1px;background:var(--blue);margin:18px 0 12px}
.card .who{font-weight:700;font-size:13px;color:var(--blue)}
.card.active{background:var(--blue)}
.card.active p,.card.active .who{color:var(--white)}
.card.active .rule{background:var(--white)}
.quote{position:absolute;left:121px;top:-28px;width:52px;height:58px;display:flex;align-items:center;justify-content:center;font-family:Georgia,serif;font-weight:700;font-size:26px}
.arrow-btn{position:absolute;top:72px;width:34px;height:34px;border-radius:50%;background:#222;color:#fff;display:flex;align-items:center;justify-content:center;font-size:18px}

/* contact */
.field-label{position:absolute;font-size:13px;color:var(--ink)}
.field{position:absolute;height:64px;border:1.5px solid #bcbcbc;border-radius:2px;background:var(--white);padding:22px 26px;font-size:11px;color:#a8a8a8}
.info{position:absolute;left:784px;width:280px;border-radius:4px;padding:34px 0 0 66px;font-size:12.5px;color:var(--ink)}
.info .lbl{font-size:12px;margin-bottom:10px}
.info b{font-weight:700;font-size:14px;line-height:24px}
.info svg{position:absolute;left:28px;top:34px}

/* footer */
.footer{left:0;top:4670px;width:1200px;height:393px;background:linear-gradient(180deg,#1e2a38 0%,#3a3a40 45%,#8a5a2a 80%,#c98a3a 100%)}
.footer a{color:var(--white);text-decoration:none;font-size:13.5px}
.social{width:30px;height:30px;border-radius:50%;background:#5e6640}
</style>
</head>
<body>

<!-- hero -->
<section class="abs hero" role="img" aria-label="Photo of a smiling woman sitting in a sunny summer meadow"></section>
<svg class="abs" style="left:0;top:560px" width="1200" height="60" viewBox="0 0 1200 60">
  <path d="M0 22 Q600 70 1200 22 L1200 60 L0 60 Z" fill="#fff"/>
  <path d="M0 22 Q600 70 1200 22 L1200 32 Q600 80 0 32 Z" fill="var(--blue)"/>
</svg>
<header>
  <div class="abs brand" style="left:140px;top:20px;color:var(--ink)"><span class="brand-mark"></span>Achtsam Leben</div>
  <a class="btn" style="left:888px;top:26px;width:170px;height:40px">Kontaktiere Uns</a>
</header>
<h1 class="abs hero-title">Mehr Glück Und<br>Zufriedenheit Im Leben</h1>
<a class="btn" style="left:140px;top:368px;width:328px;height:40px">Kostenloses Erstgespräch Vereinbaren</a>
<div class="abs hex down"></div>
<svg class="abs" style="left:591px;top:626px" width="20" height="20" viewBox="0 0 20 20"><path d="M10 3v13M4 10l6 6 6-6" stroke="#fff" stroke-width="2" fill="none"/></svg>

<!-- issue -->
<section class="abs issue">
  <h1>Leidest du unter Angstzuständen, Traumata oder emotionalen Belastungen?</h1>
  <p class="body abs" style="left:137px;top:178px;width:470px">Unser Gehirn merkt sich Erfahrungen, die schwerwiegend waren oder uns in einer traumatischen Situation überfordert haben. Wenn wir unbewusst an solche Erfahrungen erinnert werden, sind wir nicht mehr voll und ganz handlungsfähig und fühlen uns schlecht</p>
  <div class="abs" style="left:137px;top:290px;font-size:13.5px;color:var(--blue);font-weight:500">Vorteile</div>
  <div class="benefit" style="left:137px;top:324px"><svg class="tick" viewBox="0 0 18 18"><path d="M9 1l7 3v5c0 4-3 7-7 8-4-1-7-4-7-8V4z" fill="#333"/><path d="M5.5 9l2.5 2.5 4.5-4.5" stroke="#fff" stroke-width="1.8" fill="none"/></svg>Verbesserte Emotionsregulierung</div>
  <div class="benefit" style="left:408px;top:324px"><svg class="tick" viewBox="0 0 18 18"><path d="M9 1l7 3v5c0 4-3 7-7 8-4-1-7-4-7-8V4z" fill="#333"/><path d="M5.5 9l2.5 2.5 4.5-4.5" stroke="#fff" stroke-width="1.8" fill="none"/></svg>Geringere Ängste</div>
  <div class="benefit" style="left:137px;top:360px"><svg class="tick" viewBox="0 0 18 18"><path d="M9 1l7 3v5c0 4-3 7-7 8-4-1-7-4-7-8V4z" fill="#333"/><path d="M5.5 9l2.5 2.5 4.5-4.5" stroke="#fff" stroke-width="1.8" fill="none"/></svg>Größeres Selbstbewusstsein</div>
  <a class="btn" style="left:140px;top:413px;width:325px;height:56px">Kostenloses Erstgespräch Vereinbaren</a>
  <svg class="abs" style="left:655px;top:190px" width="412" height="285" viewBox="0 0 412 285">
    <polygon points="0,110 206,200 412,110 412,165 206,255 0,165" fill="var(--blue)"/>
    <polygon points="26,70 206,150 386,70 386,120 206,200 26,120" fill="#6aaa5a"/>
    <polygon points="50,30 206,100 362,30 362,80 206,150 50,80" fill="var(--yellow)"/>
  </svg>
  <div class="abs hex" style="left:703px;top:33px;width:316px;height:330px;background:linear-gradient(160deg,#e6e3df,#b9a796 60%,#6a4e3c)" role="img" aria-label="Photo of a distressed woman holding her head"></div>
</section>

<!-- services -->
<div class="abs hex" style="left:160px;top:1320px;width:360px;height:390px;background:linear-gradient(160deg,#f1ede6,#c9a58a 55%,#4a5a7a)" role="img" aria-label="Photo of a cheerful support group holding hands"></div>
<svg class="abs" style="left:296px;top:1713px" width="88" height="28"><polyline points="2,4 44,22 86,4" stroke="var(--blue)" stroke-width="9" fill="none"/></svg>
<h2 class="abs svc" style="left:610px;top:1380px">Regulierung von Emotionen</h2>
<p class="abs body" style="left:610px;top:1440px;width:440px">Mittels dieser Technik werden gezielt die im Gehirn gespeicherten Erfahrungen, die uns blockieren, positiv verändert. In der Folge gewinnst Du an Selbstvertrauen und Selbstwirksamkeit, kannst angstfrei und selbstsicher auftreten und Erfolg in allen Lebensbereichen haben.</p>
<p class="abs body" style="left:610px;top:1570px;width:440px;font-style:italic;font-weight:600;color:var(--ink)">(Anmerkung: die Technik basiert auf Augenbewegungen wie bei „Brainspotting“ oder EMDR).</p>

<h2 class="abs svc" style="left:137px;top:1800px">Systemische Strukturaufstellungen</h2>
<p class="abs body" style="left:137px;top:1862px;width:440px">Wir alle haben überkommene Prägungen und Muster, die immer wieder Konflikte verursachen oder uns ausbremsen. In einer Aufstellung werden alte Muster aufgedeckt und verändert, sodass du an Klarheit und Selbstakzeptanz gewinnst und es dir mehr und mehr gelingt, eine glückliche Partnerschaft zu führen oder sich Konflikte im Team lösen.</p>
<div class="abs hex" style="left:650px;top:1705px;width:360px;height:390px;background:linear-gradient(170deg,#f4f4f4,#d7d8da 55%,#7b7e84)" role="img" aria-label="Photo of a man with open arms breathing freely in misty landscape"></div>
<svg class="abs" style="left:786px;top:2098px" width="88" height="28"><polyline points="2,4 44,22 86,4" stroke="#4caf50" stroke-width="9" fill="none"/></svg>

<div class="abs hex" style="left:160px;top:2140px;width:360px;height:390px;background:linear-gradient(160deg,#eef0f2,#b8bcc2 55%,#5d6a78)" role="img" aria-label="Photo of a therapist comforting a client in a session"></div>
<svg class="abs" style="left:296px;top:2533px" width="88" height="28"><polyline points="2,4 44,22 86,4" stroke="var(--yellow-strong)" stroke-width="9" fill="none"/></svg>
<h2 class="abs svc" style="left:610px;top:2200px">Ego-State-Therapie</h2>
<p class="abs body" style="left:610px;top:2260px;width:440px">Wenn Kritik manchmal bei dir ein Gefühl von Hilflosigkeit oder Minderwertigkeit auslöst, du dich manchmal hin- und hergerissen fühlst oder du eine innere Stimme hörst, die dich antreibt oder kritisiert, dann ist Teilearbeit hilfreich. Durch diese Arbeit stärkst du dein Selbstwertgefühl und versöhnst dich mit deinen inneren Stimmen. Außerdem kannst du Verletzungen deines „Inneren Kindes“ heilen. Die Teilearbeit hilft dir, zu erkennen was du wirklich willst, sodass dir wichtige Entscheidungen leichter fallen.</p>

<!-- about -->
<svg class="abs" style="left:0;top:2615px" width="1200" height="520" viewBox="0 0 1200 520">
  <path d="M0 0 H612 V520 L0 455 Z" fill="var(--blue)"/>
</svg>
<div class="abs" style="left:612px;top:2615px;width:588px;height:520px;background:linear-gradient(150deg,#dfe4ec,#c5ccd8 50%,#3d63b8)" role="img" aria-label="Portrait photo of the smiling coach"></div>
<div class="abs" style="left:130px;top:2700px;font-family:'Poppins',sans-serif;font-weight:800;font-size:48px;color:var(--yellow)">Martin Hoffmann</div>
<div class="abs" style="left:134px;top:2775px;width:380px;font-weight:700;font-size:13.5px;line-height:24px;color:var(--white)">Psychotherapie, Psychoonkologie oder Coaching mit vaLumo® oder EMDR</div>
<p class="abs" style="left:134px;top:2840px;width:370px;font-size:13.5px;line-height:23px;color:var(--white)">Die Themen Heilung, persönliches Wachstum, Ganzwerdung und Selbsterkenntnis begleiten mich schon mein ganzes Leben. Ich bin seit November 2021 zertifizierter vaLumo® Coach</p>
<a class="btn" style="left:134px;top:2965px;width:136px;height:56px;background:var(--white);color:var(--ink)">Mehr Lesen</a>
<a class="btn" style="left:284px;top:2965px;width:111px;height:56px;background:transparent;border:1.5px solid var(--white)">Kontakt</a>

<!-- cta -->
<svg class="abs" style="left:465px;top:3150px" width="296" height="30"><polyline points="0,4 148,22 296,4" stroke="var(--yellow-strong)" stroke-width="6" fill="none"/></svg>
<h2 class="abs" style="left:0;top:3233px;width:1200px;text-align:center;font-family:'Plus Jakarta Sans',sans-serif;font-weight:500;font-size:38px;color:var(--ink)">Bereit, Den Ersten Schritt Zu Gehen?</h2>
<p class="abs" style="left:250px;top:3312px;width:700px;text-align:center;font-size:15px;line-height:24px;color:var(--text)">Ermutigen Sie potenzielle Kunden, ein kostenloses Beratungsgespräch zu vereinbaren, um ihre Ziele und die Möglichkeiten ihrer Dienstleistungen zu besprechen.</p>
<a class="btn" style="left:453px;top:3385px;width:324px;height:56px;background:var(--yellow);color:var(--ink)">Kostenloses Erstgespräch Vereinbaren</a>

<!-- reviews -->
<section class="abs reviews">
  <h2 class="abs svc" style="left:137px;top:72px;font-weight:500;font-size:30px">Kundenrezensionen</h2>
  <div class="arrow-btn" style="left:981px">‹</div>
  <div class="arrow-btn" style="left:1027px">›</div>
  <div class="card" style="left:137px"><div class="quote hex" style="background:var(--blue)"><span class="hex" style="width:46px;height:52px;background:#fff;display:flex;align-items:center;justify-content:center;color:var(--ink)">“</span></div><p>Lorem ipsum dolor sit amet consectetur. Aliquam id morbi lorem sit tortor tempor. Adipiscing velit tellus.</p><div class="rule"></div><div class="who">Lena Brandt</div></div>
  <div class="card active" style="left:452px"><div class="quote hex" style="background:var(--yellow);color:var(--ink)">“</div><p>Lorem ipsum dolor sit amet consectetur. Senectus aliquam mi sed velit mi ut penatibus. Id nibh mollis.</p><div class="rule"></div><div class="who">Jonas Keller</div></div>
  <div class="card" style="left:767px"><div class="quote hex" style="background:var(--blue)"><span class="hex" style="width:46px;height:52px;background:#fff;display:flex;align-items:center;justify-content:center;color:var(--ink)">“</span></div><p>Lorem ipsum dolor sit amet consectetur. Pellentesque vitae pellentesque turpis ac ac malesuada.</p><div class="rule"></div><div class="who">Mara Vogt</div></div>
</section>

<!-- contact -->
<h2 class="abs svc" style="left:137px;top:4030px;font-weight:500;font-size:34px">Kontakt Mit Uns</h2>
<div class="field-label" style="left:137px;top:4113px">Vorname</div>
<div class="field" style="left:137px;top:4143px;width:295px">Hier tippen</div>
<div class="field-label" style="left:455px;top:4113px">Nachname</div>
<div class="field" style="left:455px;top:4143px;width:292px">Hier tippen</div>
<div class="field-label" style="left:137px;top:4243px">Rufnummer</div>
<div class="field" style="left:137px;top:4273px;width:295px">Hier tippen</div>
<div class="field-label" style="left:455px;top:4243px">E-Mail Adresse</div>
<div class="field" style="left:455px;top:4273px;width:292px">Hier tippen</div>
<div class="field-label" style="left:137px;top:4373px">Ihre Nachricht</div>
<div class="field" style="left:137px;top:4403px;width:607px;height:116px">Geben Sie Ihre Nachricht ein</div>
<a class="btn" style="left:137px;top:4550px;width:185px;height:62px;font-size:14px">Einreichen</a>

<div class="info" style="top:4112px;height:183px;background:var(--card-grey)">
  <svg width="22" height="26" viewBox="0 0 22 26"><path d="M11 1a9 9 0 0 0-9 9c0 7 9 15 9 15s9-8 9-15a9 9 0 0 0-9-9z" fill="var(--blue)"/><circle cx="11" cy="10" r="3.5" fill="#fff"/></svg>
  <div class="lbl">Adresse</div>
  <b style="color:var(--blue)">Martin Hoffmann</b><br><b>Am Birkenhain 14<br>38100 Lindenstadt</b>
</div>
<div class="info" style="top:4312px;height:143px;background:var(--yellow-strong)">
  <svg width="22" height="22" viewBox="0 0 22 22"><path d="M5 2l4 4-2 3c1 3 4 6 7 7l3-2 4 4-3 3C9 21 1 13 2 5z" fill="var(--ink)"/></svg>
  <div class="lbl">Telefonnummer</div>
  <b>M: 0151 000 12 345</b>
</div>
<div class="info" style="top:4475px;height:136px;background:var(--card-grey)">
  <svg width="24" height="18" viewBox="0 0 24 18"><rect x="1" y="1" width="22" height="16" fill="var(--blue)"/><path d="M1 1l11 9 11-9" stroke="#fff" stroke-width="1.6" fill="none"/></svg>
  <div class="lbl">E-Mail Adresse</div>
  <b>kontakt@achtsam-leben.de</b>
</div>

<!-- footer -->
<footer class="abs footer" role="img" aria-label="Photo of a lone tree on a hill at sunset">
</footer>
<svg class="abs" style="left:0;top:4665px" width="1200" height="60" viewBox="0 0 1200 60"><path d="M0 0 H1200 V40 L900 20 L700 35 L600 15 L420 32 L250 20 L0 42 Z" fill="#fff"/></svg>
<div class="abs brand" style="left:150px;top:4790px;color:var(--white)"><span class="brand-mark"></span>Achtsam Leben</div>
<p class="abs" style="left:137px;top:4884px;width:350px;font-size:12.5px;line-height:23px;color:#b8b8b8">Unser Gehirn merkt sich Erfahrungen, die schwerwiegend waren oder uns in einer traumatischen Situation überfordert haben.</p>
<nav class="abs" style="left:780px;top:4810px;display:flex;gap:40px"><a>Startseite</a><a>Über mich</a><a>Kontakt</a></nav>
<div class="abs" style="left:798px;top:4865px;display:flex;align-items:center;gap:12px;color:var(--white);font-size:13.5px">Folge uns auf
  <span class="social"></span><span class="social" style="background:var(--yellow)"></span><span class="social"></span><span class="social"></span>
</div>
<div class="abs" style="left:0;top:5010px;width:1200px;text-align:center;font-size:12px;color:#d8d8d8">Urheberrecht 2024. Achtsam Leben. Alle Rechte vorbehalten.</div>
</body>
</html>
```